Creative Businesss Card desgin!

Create a business card for our business Gleam window cleaning!
We are open to creative ideas as long as it maintains a professional image.

Target Market(s)

Small Commercial window cleaning clients including car dealerships, strata manager, cafe

Industry/Entity Type

Window Cleaning

Contact Information for Business Card

Daniel Prescott
General Manager
Gleam Window Cleaning

daniel@gleamservices.com.au
pane-care-southbank.com.au
Ph: 1800 GET GLEAM
Mob: 0437 582 061

Colors
fbed22
0392cd

Requirements
Should not have
• Stock window cleaning/ squeegee graphics

```html
<!DOCTYPE html>
<html lang="en">
<head>
<meta charset="utf-8">
<title>Gleam Window Cleaning – Business Card</title>
<link href="https://fonts.googleapis.com/css2?family=Arimo:wght@400;700&display=swap" rel="stylesheet">
<style>
  :root {
    --backdrop: #1a1c1f;
    --card-light: #0a86b3;
    --card-mid: #03668f;
    --card-dark: #044a73;
    --brand-yellow: #e0d322;
    --rule-white: #e9eef2;
    --text-soft: #d7e2ea;
  }
  * { box-sizing: border-box; margin: 0; padding: 0; }
  html, body {
    width: 1200px; height: 900px; overflow: hidden;
    background: var(--backdrop);
    font-family: "Arimo", Arial, sans-serif;
  }
  .canvas {
    width: 1200px; height: 900px;
    display: flex; align-items: center; justify-content: center;
  }
  .card {
    position: relative;
    width: 1000px; height: 572px;
    background: radial-gradient(ellipse at 62% 60%, var(--card-light) 0%, var(--card-mid) 45%, var(--card-dark) 100%);
    overflow: hidden;
  }
  .brand {
    position: absolute; left: 78px; top: 62px;
    color: var(--brand-yellow);
    font-weight: 700; text-transform: uppercase;
    line-height: 1;
  }
  .brand-name { font-size: 104px; letter-spacing: 4px; display: block; }
  .brand-tag { font-size: 31px; letter-spacing: 2px; display: block; margin-top: 4px; }
  .person { position: absolute; left: 78px; top: 238px; }
  .person-name {
    color: var(--brand-yellow); font-weight: 700; font-size: 27px;
    text-transform: uppercase; letter-spacing: 1px;
  }
  .person-role { color: var(--text-soft); font-size: 21px; margin-top: 6px; }
  .divider {
    position: absolute; left: 0; right: 0; top: 318px; height: 2px;
    background: linear-gradient(90deg, var(--brand-yellow) 0%, var(--brand-yellow) 32%, var(--rule-white) 42%, var(--rule-white) 100%);
  }
  .contacts { position: absolute; left: 78px; top: 342px; list-style: none; }
  .contact {
    display: flex; align-items: center; gap: 14px;
    color: var(--rule-white); font-size: 21px; line-height: 1; margin-bottom: 12px;
  }
  .contact-icon { width: 18px; height: 18px; flex: none; }
  .contact-icon * { fill: none; stroke: var(--brand-yellow); stroke-width: 1.6; }
</style>
</head>
<body>
<main class="canvas">
  <section class="card" aria-label="Gleam Window Cleaning business card">
    <h1 class="brand">
      <span class="brand-name">Gleam</span>
      <span class="brand-tag">Window Cleaning</span>
    </h1>

    <div class="person">
      <p class="person-name">Daniel Prescott</p>
      <p class="person-role">General Manager</p>
    </div>

    <div class="divider"></div>

    <ul class="contacts">
      <li class="contact">
        <svg class="contact-icon" viewBox="0 0 18 18"><path d="M4 2l3 3-2 2c1 2 3 4 5 5l2-2 3 3-2 3C7 16 2 11 2 4z"/></svg>
        1800 GET GLEAM
      </li>
      <li class="contact">
        <svg class="contact-icon" viewBox="0 0 18 18"><rect x="5" y="1.5" width="8" height="15" rx="1.5"/><line x1="8" y1="14" x2="10" y2="14"/></svg>
        0437 582 061
      </li>
      <li class="contact">
        <svg class="contact-icon" viewBox="0 0 18 18"><rect x="1.5" y="4" width="15" height="10"/><path d="M1.5 4l7.5 6 7.5-6"/></svg>
        daniel@gleamservices.com.au
      </li>
      <li class="contact">
        <svg class="contact-icon" viewBox="0 0 18 18"><circle cx="9" cy="9" r="7.5"/><ellipse cx="9" cy="9" rx="3.2" ry="7.5"/><line x1="1.5" y1="9" x2="16.5" y2="9"/></svg>
        pane-care-southbank.com.au
      </li>
    </ul>
  </section>
</main>
</body>
</html>
```